Business Card Design

I need a business card design for a new company based in Sydney called 'The Copper Ladle'. We deliver organic, gourmet and fine foods to your door.

I would like to see creative, unique designs which use colours which represent health and nature like green.

Target Market(s)

Health conscious 20 to 35 year olds.

Industry/Entity Type

Health

Contact Information for Business Card

The Copper Ladle, Owen Barclett, owen@thecopperladle.com.au, 0427685392

Requirements
Must have
• My logo.

```html
<!DOCTYPE html>
<html lang="en">
<head>
<meta charset="utf-8">
<title>The Copper Ladle – Business Card</title>
<link rel="stylesheet" href="https://fonts.googleapis.com/css2?family=Jost:wght@300;400&family=Open+Sans:wght@700&display=swap">
<style>
  :root {
    --page: #ffffff;
    --card-edge: #b9b9b9;
    --brand-green: #3aa614;
    --lime: #8fe01a;
    --forest: #177a0d;
    --deep: #0f6a09;
    --bright: #86ec12;
    --white: #ffffff;
  }
  * { margin: 0; padding: 0; box-sizing: border-box; }
  html, body {
    width: 989px; height: 1200px; overflow: hidden;
    background: var(--page);
  }
  .sheet { position: relative; width: 989px; height: 1200px; }

  .card {
    position: absolute;
    left: 77px; width: 835px; height: 463px;
    border-radius: 28px;
  }
  .card--front {
    top: 113px;
    background: var(--page);
    border: 1.5px solid var(--card-edge);
  }
  .card--back {
    top: 623px;
    background:
      radial-gradient(circle at 83% 15%, var(--bright) 0%, #5ec70f 22%, #2f9a0e 50%, var(--forest) 72%, var(--deep) 100%);
    border: 1.5px solid #4a8f2e;
    overflow: hidden;
  }

  /* Front wordmark */
  .wordmark {
    position: absolute; left: 125px; top: 140px;
    display: flex; align-items: center; gap: 34px;
  }
  .wordmark__dot {
    width: 170px; height: 170px; border-radius: 50%;
    background: var(--lime);
  }
  .wordmark__name {
    font-family: "Jost", sans-serif; font-weight: 300;
    font-size: 82px; line-height: 0.98; letter-spacing: -1px;
    color: var(--brand-green);
  }

  /* Back */
  .mini-mark {
    position: absolute; left: 150px; top: 165px;
    display: flex; flex-direction: column; align-items: center; gap: 12px;
  }
  .mini-mark__dot {
    width: 112px; height: 112px; border-radius: 50%;
    background: var(--lime);
  }
  .mini-mark__name {
    font-family: "Jost", sans-serif; font-weight: 300;
    font-size: 17px; color: var(--white); white-space: nowrap;
  }
  .divider {
    position: absolute; left: 374px; top: 120px;
    width: 3px; height: 265px;
    background: linear-gradient(to bottom, transparent, rgba(190,255,120,0.9) 50%, transparent);
  }
  .contact {
    position: absolute; left: 411px; top: 165px;
    color: var(--white);
    text-shadow: 2px 3px 4px rgba(0,0,0,0.35);
  }
  .contact__name {
    font-family: "Jost", sans-serif; font-weight: 300;
    font-size: 42px; line-height: 1.1; letter-spacing: 0.5px;
  }
  .contact__email {
    font-family: "Jost", sans-serif; font-weight: 400;
    font-size: 24px; line-height: 1.2;
  }
  .contact__phone {
    margin-top: 50px;
    font-family: "Open Sans", sans-serif; font-weight: 700;
    font-size: 30px;
  }
</style>
</head>
<body>
<main class="sheet">
  <section class="card card--front">
    <div class="wordmark">
      <span class="wordmark__dot" aria-hidden="true"></span>
      <span class="wordmark__name">The Copper<br>Ladle</span>
    </div>
  </section>

  <section class="card card--back">
    <div class="mini-mark">
      <span class="mini-mark__dot" aria-hidden="true"></span>
      <span class="mini-mark__name">The Copper Ladle</span>
    </div>
    <span class="divider" aria-hidden="true"></span>
    <div class="contact">
      <p class="contact__name">Owen Barclett</p>
      <p class="contact__email">owen@thecopperladle.com.au</p>
      <p class="contact__phone">0427 685 392</p>
    </div>
  </section>
</main>
</body>
</html>
```